Parkinson's Disease Progression

Visually describe the rate of Parkinson progression in the first 15 years following diagnosis. Title: "Patient-Perceived Progression of Parkinsonism"

The attached figure names "meanqol" is the curve that should serve as the basis of this graphic. Everything else-- color, labels, font, etc. describe this curve.
Thank you!

Target Market(s)

People with Parkisnon's Disease, neurologists, family members.

Font styles to use
Sans Serif

Requirements
Must have
• Must have the lines going through these exact numbers
Excellent -- 502
Very good- 661
Good- 895
Fair- 1268
Poor- 1655

LABELS:
Title: "Patient-Perceived Progression of Parkinsonism"
"SAW-MX (Self-Assessed Wellbeing Index for Movement Conditions)" should be the label on the left.
"Quality of Life" should be the label on the right
"Years Since Diagnosis" should be the label on the bottom
Nice to have
• A color scheme that goes from GOOD (low numbers) to BAD (high numbers).

Easy to read (elderly)

```html
<!DOCTYPE html>
<html lang="en">
<head>
<meta charset="utf-8">
<title>Patient-Perceived Progression of Parkinsonism</title>
<link rel="stylesheet" href="https://fonts.googleapis.com/css2?family=Source+Sans+3:ital,wght@0,400;0,600;0,700;1,600;1,700&display=swap">
<style>
  :root {
    --page: #ffffff;
    --frame: #cfcfcf;
    --title-bar: #65655f;
    --title-text: #e4d772;
    --panel-yellow: #fce419;
    --grid: #cfc9ad;
    --axis-text: #8a8a8a;
    --label-dark: #333333;
    --qol-blue: #0b6fb6;
    --band-line: #1d6f8e;
    --curve: #93278f;
  }
  html, body {
    margin: 0;
    padding: 0;
    width: 1200px;
    height: 1200px;
    overflow: hidden;
    background: var(--page);
  }
  .chart-canvas {
    display: block;
    width: 1200px;
    height: 1200px;
    font-family: "Source Sans 3", sans-serif;
  }
  .chart-title { fill: var(--title-text); font-size: 24px; font-weight: 600; }
  .tick-label { fill: var(--axis-text); font-size: 17.5px; font-weight: 600; }
  .axis-title { fill: var(--label-dark); font-size: 24px; font-weight: 600; }
  .axis-subtitle { fill: var(--label-dark); font-size: 11.5px; font-weight: 600; }
  .band-label { fill: var(--qol-blue); font-size: 12.5px; font-style: italic; font-weight: 600; }
  .qol-title { fill: var(--qol-blue); font-size: 25px; font-style: italic; font-weight: 700; }
  .grid-line { stroke: var(--grid); stroke-width: 1.2; }
  .band-line { stroke: var(--band-line); stroke-width: 1; stroke-dasharray: 8 6; }
  .mean-curve { fill: none; stroke: var(--curve); stroke-width: 3.6; stroke-linecap: round; stroke-linejoin: round; }
  .interval-curve { fill: none; stroke: var(--curve); stroke-width: 1.3; stroke-dasharray: 4 3; stroke-linejoin: round; }
</style>
</head>
<body>
<svg class="chart-canvas" viewBox="0 0 1200 1200" xmlns="http://www.w3.org/2000/svg">
  <defs>
    <radialGradient id="glow" cx="506" cy="531" r="260" gradientUnits="userSpaceOnUse">
      <stop offset="0" stop-color="#ffffff"/>
      <stop offset="0.35" stop-color="#fff4a8"/>
      <stop offset="1" stop-color="#fce419"/>
    </radialGradient>
    <linearGradient id="dusk" x1="0" y1="219" x2="0" y2="360" gradientUnits="userSpaceOnUse">
      <stop offset="0" stop-color="#65655f"/>
      <stop offset="1" stop-color="#fce419" stop-opacity="0"/>
    </linearGradient>
    <clipPath id="panel-clip">
      <rect x="302" y="170" width="656" height="503" rx="12"/>
    </clipPath>
  </defs>

  <!-- outer card -->
  <rect x="119" y="136" width="964" height="617" rx="12" fill="var(--page)" stroke="var(--frame)" stroke-width="2"/>

  <!-- plot panel -->
  <g clip-path="url(#panel-clip)">
    <rect x="302" y="170" width="656" height="503" fill="var(--panel-yellow)"/>
    <rect x="302" y="170" width="656" height="503" fill="url(#glow)"/>
    <rect x="302" y="219" width="656" height="160" fill="url(#dusk)"/>
    <rect x="302" y="170" width="656" height="49" fill="var(--title-bar)"/>
  </g>
  <text class="chart-title" x="632" y="202" text-anchor="middle">Patient-Perceived Progression of Parkinsonism</text>

  <!-- grid -->
  <g class="grid">
    <line class="grid-line" x1="297" y1="285" x2="968" y2="285"/>
    <line class="grid-line" x1="297" y1="351" x2="968" y2="351"/>
    <line class="grid-line" x1="297" y1="417" x2="968" y2="417"/>
    <line class="grid-line" x1="297" y1="483" x2="968" y2="483"/>
    <line class="grid-line" x1="297" y1="549" x2="968" y2="549"/>
    <line class="grid-line" x1="297" y1="616" x2="968" y2="616"/>
    <line class="grid-line" x1="335" y1="219" x2="335" y2="681"/>
    <line class="grid-line" x1="530" y1="219" x2="530" y2="681"/>
    <line class="grid-line" x1="726" y1="219" x2="726" y2="681"/>
    <line class="grid-line" x1="921" y1="219" x2="921" y2="681"/>
  </g>

  <!-- y ticks -->
  <g class="y-ticks" text-anchor="end">
    <text class="tick-label" x="292" y="291">1200</text>
    <text class="tick-label" x="292" y="357">1000</text>
    <text class="tick-label" x="292" y="423">800</text>
    <text class="tick-label" x="292" y="489">600</text>
    <text class="tick-label" x="292" y="555">400</text>
    <text class="tick-label" x="292" y="622">200</text>
  </g>

  <!-- x ticks -->
  <g class="x-ticks" text-anchor="middle">
    <text class="tick-label" x="335" y="702">0</text>
    <text class="tick-label" x="530" y="702">5</text>
    <text class="tick-label" x="726" y="702">10</text>
    <text class="tick-label" x="921" y="702">15</text>
  </g>

  <!-- quality of life bands -->
  <g class="bands">
    <line class="band-line" x1="309" y1="269" x2="950" y2="269"/>
    <line class="band-line" x1="309" y1="389" x2="950" y2="389"/>
    <line class="band-line" x1="309" y1="462" x2="950" y2="462"/>
    <line class="band-line" x1="309" y1="522" x2="950" y2="522"/>
    <text class="band-label" x="961" y="247">Poor</text>
    <text class="band-label" x="961" y="275">Fair</text>
    <text class="band-label" x="961" y="396">Good</text>
    <text class="band-label" x="961" y="467">Very good</text>
    <text class="band-label" x="961" y="527">Excellent</text>
  </g>

  <!-- curves -->
  <path class="interval-curve" d="M325 508 C345 504 360 501 375 497 C400 488 418 478 438 469 C460 458 480 448 500 444 C525 436 545 434 563 433 C585 431 600 431 613 430 C628 428 640 424 650 420 C680 410 700 394 725 381 C750 368 768 358 788 350 C815 338 840 330 863 320 C890 308 912 292 936 275"/>
  <path class="interval-curve" d="M325 576 C340 561 358 545 375 531 C395 515 415 502 438 491 C470 473 500 462 525 456 C550 451 575 450 594 450 C612 448 630 446 644 443 C675 436 700 421 725 409 C750 397 768 388 788 381 C815 371 845 362 875 363 C900 364 920 366 936 371"/>
  <path class="mean-curve" d="M321 544 C340 533 358 523 375 513 C398 500 418 487 438 475 C462 462 484 452 506 448 C530 443 555 443 581 443 C605 443 622 439 638 434 C670 424 700 407 725 394 C748 382 768 373 788 366 C810 357 830 350 850 345 C880 337 910 330 936 324"/>

  <!-- left axis title -->
  <g class="left-label" text-anchor="end">
    <text class="axis-title" x="244" y="423">SAW-MX</text>
    <text class="axis-subtitle" x="241" y="442">(Self-Assessed Wellbeing</text>
    <text class="axis-subtitle" x="241" y="455">Index for Movement</text>
    <text class="axis-subtitle" x="241" y="468">Conditions)</text>
  </g>

  <!-- right axis title -->
  <g class="right-label">
    <text class="qol-title" x="978" y="424">Quality</text>
    <text class="qol-title" x="978" y="448">of Life</text>
  </g>

  <!-- bottom axis title -->
  <g class="bottom-label" text-anchor="middle">
    <text class="axis-title" x="627" y="703">Years Since</text>
    <text class="axis-title" x="627" y="727">Diagnosis</text>
  </g>
</svg>
</body>
</html>
```